Powerpoint Presentation Template

Kindly design a business class Powepoint Presentation template for our business use. Please stick to our company colours or even pictures as shown on our website and Logo

```html
<!DOCTYPE html>
<html lang="en">
<head>
<meta charset="utf-8">
<title>Meridane Properties – Presentation Template</title>
<link href="https://fonts.googleapis.com/css2?family=Montserrat:wght@300;400;500;600;700&display=swap" rel="stylesheet">
<style>
:root{
  --red:#8a2e23;
  --red-deep:#7a261d;
  --red-soft:#e6a493;
  --ink:#3b3b3b;
  --muted:#777;
  --line:#d9d9d9;
  --paper:#ffffff;
  --canvas-top:#f1f1f1;
  --canvas-bottom:#dcdcdc;
  --sky:#6d9bd8;
  --concrete:#9aa3ad;
  --brick:#a8826a;
  --dusk:#c8a98f;
}
*{box-sizing:border-box;margin:0;padding:0}
html,body{width:1200px;height:831px;overflow:hidden}
body{
  position:relative;
  font-family:"Montserrat",sans-serif;
  color:var(--ink);
  background:linear-gradient(180deg,var(--canvas-top),var(--canvas-bottom));
}
.slide{position:absolute;background:var(--paper);overflow:hidden;box-shadow:0 1px 3px rgba(0,0,0,.08)}
.slide.sm{width:240px;height:166px}
.abs{position:absolute}
.title{position:absolute;left:10px;top:19px;font-size:11px;font-weight:400;color:var(--red);letter-spacing:.2px;white-space:nowrap}
.tiny{font-size:3.4px;line-height:1.45;color:var(--ink)}
.tiny.w{color:#fff}
.photo{position:absolute}
.brand{position:absolute;right:17px;bottom:3px;font-size:4.4px;line-height:1.05;font-weight:700;color:var(--red);text-align:right}
.corner{position:absolute;right:0;bottom:0;width:22px;height:12px;background:var(--red);clip-path:polygon(0 0,100% 100%,0 100%)}

/* cover */
.cover{left:61px;top:33px;width:529px;height:365px}
.cover .shot{inset:0;clip-path:polygon(0 80px,403px 0,256px 365px,0 365px);
  background:linear-gradient(170deg,var(--sky) 0%,#8fb2e0 22%,var(--concrete) 45%,#6f7780 70%,var(--brick) 100%)}
.cover .wedge{inset:0;background:var(--red);clip-path:polygon(403px 0,529px 0,529px 365px,256px 365px)}
.cover .brand-lg{left:19px;top:18px;font-size:20px;font-weight:600;color:var(--red);line-height:1.05}
.cover .motto{right:14px;top:20px;text-align:right;color:var(--red-soft)}
.cover .motto b{display:block;font-size:11px;font-weight:600}
.cover .motto span{font-size:6.5px}
.cover .sub{left:317px;top:236px;font-size:24px;color:#fff;font-weight:300}
.cover .main{left:302px;top:265px;font-size:25px;color:#fff;font-weight:700;white-space:nowrap}
.cover .date{left:295px;top:298px;font-size:11px;color:#fff;font-weight:300}
.cover .foot{left:271px;top:344px;font-size:6.2px;color:#f3d6cf;white-space:nowrap}

/* contents */
.toc .shot{left:0;top:0;width:96px;height:166px;background:linear-gradient(100deg,#b6bcc3,#e4e7ea 55%,#8a939c)}
.toc .head{left:106px;top:37px;font-size:10.5px;color:var(--red);font-weight:400}
.toc .item{position:absolute;font-size:3.5px;line-height:1.4;color:var(--ink);width:60px}
.toc .item b{font-size:7.5px;color:var(--red);font-weight:600}

.big{position:absolute;left:16px;top:39px;font-size:18.5px;line-height:1.05;color:var(--red);font-weight:400}
.big small{display:block;font-size:6.5px;color:var(--ink);margin-top:4px}

/* intro */
.intro .shot{inset:0 0 13px 0;background:linear-gradient(180deg,#9fbbe0 0%,#c5d6ea 45%,var(--dusk) 62%,#b76a4d 78%,#8d7b5e 100%)}
.intro .col{top:41px;width:104px}

/* achievements */
.achv .quote{left:10px;top:38px;width:56px;height:110px;background:#f4f2f1;color:var(--red);font-size:4.6px;text-align:center;padding:34px 3px 0;line-height:1.3}
.achv .quote::before{content:"";position:absolute;left:21px;top:10px;width:14px;height:14px;border-radius:50%;background:#e4d9d6}
.badges{position:absolute;left:70px;top:110px;width:160px;display:flex;justify-content:space-between}
.badges span{width:30px;display:flex;flex-direction:column;align-items:center;gap:3px;font-size:2.8px;text-align:center;color:var(--ink)}
.badges i{display:block;width:16px;height:16px;border-radius:50%;border:1.3px solid var(--red)}

/* services */
.svc .pic{top:35px;width:72px;height:68px}
.svc .tag{position:absolute;right:0;bottom:0;background:var(--red);color:#fff;font-size:4.4px;font-weight:700;padding:1px 3px;text-align:right}
.svc ul{position:absolute;top:107px;width:70px;list-style:disc;padding-left:5px}

/* grid */
.cell{position:absolute;width:55px;height:52px}
.cell.red{background:var(--red);color:#fff;text-align:center;padding:6px 4px}
.cell.red b{display:block;font-size:3.6px;margin-bottom:2px}

/* timeline */
.tl-line{left:14px;top:82px;width:214px;height:.8px;background:var(--red)}
.dot{position:absolute;width:13px;height:13px;border-radius:50%;background:var(--red);border:1.5px solid #e8c0b7;color:#fff;font-size:3.4px;display:flex;align-items:center;justify-content:center}
.tick{position:absolute;width:2px;height:2px;border-radius:50%;background:var(--red)}

/* feature */
.feat .shot{left:10px;top:38px;width:220px;height:112px;background:linear-gradient(180deg,#c6cfd9,#e3d3c4 45%,#b3876a 70%,#8c7a63)}
.feat .panel{left:10px;top:38px;width:103px;height:112px;background:rgba(138,46,35,.82);padding:5px 6px}

/* icon columns */
.ic{position:absolute;top:46px;width:50px}
.ic .bar{height:24px;background:var(--red);position:relative;clip-path:polygon(0 0,100% 0,100% 100%,8% 100%,0 80%)}
.ic .sq{position:absolute;left:4px;top:4px;width:12px;height:12px;border:1px solid #fff}
.ic .lab{position:absolute;right:4px;top:7px;color:#fff;font-size:5px;font-weight:700;line-height:1.05;text-align:center}
.ic p{margin-top:5px;text-align:center}

/* table */
.tbl .thumb{top:38px;width:41px;height:34px}
.row{position:absolute;left:14px;width:216px;height:.5px;background:var(--line)}

/* charts */
.hdr{position:absolute;height:8px;background:var(--red)}

/* thank you */
.thanks .shot{left:0;top:0;width:240px;height:102px;background:linear-gradient(170deg,#4f86cf,#93b7e3 40%,#dfe3e6 60%,#8f969c);clip-path:polygon(0 0,100% 0,100% 100%,0 78%)}
.thanks .bye{right:12px;top:13px;font-size:11px;font-weight:700;color:#fff}
.thanks .strip{left:0;bottom:0;width:240px;height:12px;background:var(--red);clip-path:polygon(0 0,56% 0,60% 100%,0 100%)}
.thanks .strip2{left:0;bottom:0;width:240px;height:12px;background:var(--red-deep);clip-path:polygon(58% 40%,100% 40%,100% 100%,62% 100%)}
</style>
</head>
<body>

<!-- Cover -->
<section class="slide cover">
  <div class="abs shot" role="img" aria-label="Photo of a modern multi-storey residential building against a blue sky"></div>
  <div class="abs wedge"></div>
  <div class="abs brand-lg">MERIDANE<br>Properties</div>
  <div class="abs motto"><b>Building Beyond</b><span>A member of the Meridane Group</span></div>
  <div class="abs sub">Sub-title</div>
  <div class="abs main">Powerpoint Title</div>
  <div class="abs date">July 2018</div>
  <div class="abs foot">www.meridane.com / info@meridane.com / +27 11 555 0142</div>
</section>

<!-- Contents -->
<section class="slide sm toc" style="left:626px;top:33px">
  <div class="photo shot" role="img" aria-label="Photo of white apartment balconies"></div>
  <div class="abs head">Contents</div>
  <div class="item" style="left:106px;top:53px"><b>03</b>/ Lorem ipsum dolor sit amet dolor</div>
  <div class="item" style="left:176px;top:53px"><b>15</b>/ Lorem ipsum dolor sit amet dolor</div>
  <div class="item" style="left:106px;top:72px"><b>06</b>/ Lorem ipsum dolor sit amet dolor</div>
  <div class="item" style="left:176px;top:72px"><b>18</b>/ Lorem ipsum dolor sit amet dolor</div>
  <div class="item" style="left:106px;top:92px"><b>09</b>/ Lorem ipsum dolor sit amet dolor</div>
  <div class="item" style="left:176px;top:92px"><b>21</b>/ Lorem ipsum dolor sit amet dolor</div>
  <div class="item" style="left:106px;top:112px"><b>12</b>/ Lorem ipsum dolor sit amet dolor</div>
  <div class="brand">MERIDANE<br>Properties</div><div class="corner"></div>
</section>

<!-- Section divider -->
<section class="slide sm" style="left:898px;top:33px">
  <div class="big">Lorem ipsum<br>dolor sit amet<small>Lorem ipsum dolor sit amet</small></div>
  <div class="brand">MERIDANE<br>Properties</div><div class="corner"></div>
</section>

<!-- Introduction -->
<section class="slide sm intro" style="left:626px;top:233px">
  <div class="photo shot" role="img" aria-label="Photo of a row of new orange-roofed homes at dusk"></div>
  <div class="title">Introduction</div>
  <p class="abs tiny col" style="left:12px">/ Lorem ipsum dolor sit amet, our company is a property group focused on building and development, with a strong base of sound and careful skill.<br>/ As a property group, we believe both public and private bodies play their role in the growth of our region. We continue to</p>
  <p class="abs tiny col" style="left:124px">pursue chances to offer sound and fair housing, retail spaces and public works, with strong value to our clients and to the towns in which we work.</p>
  <div class="brand">MERIDANE<br>Properties</div><div class="corner"></div>
</section>

<!-- Achievements -->
<section class="slide sm achv" style="left:898px;top:233px">
  <div class="title">Achievements</div>
  <div class="abs quote">Lorem ipsum dolor sit amet, consectetur adipiscing elit, sed do eiusmod tempor</div>
  <p class="abs tiny" style="left:70px;top:38px;width:160px;font-size:3px">We are proud to take part in delivering housing and bulk services, and to give young people a path into our growing management team.<br>We employ skilled staff across a wide range of trades, and our network lets us train and hold the high level of care needed to meet our own standards of delivery and efficiency.<br>From schools and clinics to offices and houses, our projects span roads, bridges, water works and drainage, as well as full township layouts and secure villages.</p>
  <div class="badges">
    <span><i></i>Housing award</span><span><i></i>Service award</span><span><i></i>Build award</span><span><i></i>Design award</span><span><i></i>Quality award</span>
  </div>
  <div class="brand">MERIDANE<br>Properties</div><div class="corner"></div>
</section>

<!-- Services -->
<section class="slide sm svc" style="left:61px;top:433px">
  <div class="title">Our Services</div>
  <div class="photo pic" style="left:10px;background:linear-gradient(160deg,#6f87a8,#8b6b55)" role="img" aria-label="Photo of a building under construction"><span class="tag">Building<br>Construction</span></div>
  <div class="photo pic" style="left:85px;background:linear-gradient(160deg,#c79a6e,#a8643e)" role="img" aria-label="Photo of workers on a road site"><span class="tag">Road &amp; Civil<br>Construction</span></div>
  <div class="photo pic" style="left:160px;background:linear-gradient(160deg,#8fa9c6,#6b6f73)" role="img" aria-label="Photo of a modern property development"><span class="tag">Property<br>Development</span></div>
  <ul class="tiny" style="left:12px"><li>Lorem ipsum dolor sit amet, consectetur adipiscing elit.</li><li>Nam sit amet dictum neque, pretium fringilla metus.</li></ul>
  <ul class="tiny" style="left:87px"><li>Lorem ipsum dolor sit amet, consectetur adipiscing elit.</li><li>Nam sit amet dictum neque, pretium fringilla metus.</li></ul>
  <ul class="tiny" style="left:162px"><li>Lorem ipsum dolor sit amet, consectetur adipiscing elit.</li><li>Nam sit amet dictum neque, pretium fringilla metus.</li></ul>
  <div class="brand">MERIDANE<br>Properties</div><div class="corner"></div>
</section>

<!-- Image grid -->
<section class="slide sm" style="left:341px;top:433px">
  <div class="title">Lorem ipsum dolor sit amet</div>
  <div class="cell photo" style="left:10px;top:34px;background:linear-gradient(160deg,#9db8d6,#66707a)" role="img" aria-label="Photo of apartment facade"></div>
  <div class="cell red tiny w" style="left:65px;top:34px"><b>Title</b>Lorem ipsum dolor sit amet, consectetur adipiscing elit. Nam sit amet dictum neque.</div>
  <div class="cell photo" style="left:120px;top:34px;background:linear-gradient(160deg,#a9c3e3,#8d8f8a)" role="img" aria-label="Photo of a residential street"></div>
  <div class="cell red tiny w" style="left:175px;top:34px"><b>Title</b>Lorem ipsum dolor sit amet, consectetur adipiscing elit. Nam sit amet dictum neque.</div>
  <div class="cell red tiny w" style="left:10px;top:86px"><b>Title</b>Lorem ipsum dolor sit amet, consectetur adipiscing elit.</div>
  <div class="cell photo" style="left:65px;top:86px;background:linear-gradient(160deg,#7d8791,#4a8fc2)" role="img" aria-label="Photo of a building with pool"></div>
  <div class="cell red tiny w" style="left:120px;top:86px"><b>Title</b>Lorem ipsum dolor sit amet, consectetur adipiscing elit.</div>
  <div class="cell photo" style="left:175px;top:86px;background:linear-gradient(160deg,#c7ced4,#5f6b63)" role="img" aria-label="Photo of modern houses"></div>
  <div class="brand">MERIDANE<br>Properties</div><div class="corner"></div>
</section>

<!-- Timeline -->
<section class="slide sm" style="left:619px;top:433px">
  <div class="title">Timeline</div>
  <div class="abs tl-line"></div>
  <div class="tick" style="left:13px;top:81px"></div>
  <div class="dot" style="left:21px;top:47px">Year</div><div class="dot" style="left:75px;top:47px">Year</div><div class="dot" style="left:130px;top:47px">Year</div><div class="dot" style="left:185px;top:47px">Year</div>
  <div class="dot" style="left:47px;top:115px">Year</div><div class="dot" style="left:102px;top:115px">Year</div><div class="dot" style="left:156px;top:115px">Year</div>
  <p class="abs tiny" style="left:26px;top:62px;width:36px">Lorem ipsum dolor sit amet, consectetur adipiscing elit.</p>
  <p class="abs tiny" style="left:90px;top:47px;width:26px">Lorem ipsum dolor sit amet, consectetur adipiscing elit.</p>
  <p class="abs tiny" style="left:134px;top:62px;width:36px">Lorem ipsum dolor sit amet, consectetur adipiscing elit.</p>
  <p class="abs tiny" style="left:200px;top:47px;width:26px">Lorem ipsum dolor sit amet, consectetur adipiscing elit.</p>
  <p class="abs tiny" style="left:52px;top:92px;width:36px">Lorem ipsum dolor sit amet, consectetur adipiscing elit.</p>
  <p class="abs tiny" style="left:106px;top:92px;width:36px">Lorem ipsum dolor sit amet, consectetur adipiscing elit.</p>
  <p class="abs tiny" style="left:161px;top:92px;width:36px">Lorem ipsum dolor sit amet, consectetur adipiscing elit.</p>
  <div class="brand">MERIDANE<br>Properties</div><div class="corner"></div>
</section>

<!-- Feature image -->
<section class="slide sm feat" style="left:898px;top:433px">
  <div class="title">Lorem ipsum dolor sit amet</div>
  <div class="photo shot" role="img" aria-label="Photo of a new house on an open plot at sunset"></div>
  <p class="abs panel tiny w">/ Lorem ipsum dolor sit amet, consectetur adipiscing elit.<br>/ Nam sit amet dictum neque, pretium fringilla metus. Nam bibendum urna in pharetra vehicula.<br>/ Aenean luctus leo vitae quam elementum, ut semper libero faucibus. Maecenas eu magna sodales, finibus nisi vitae, finibus felis. Morbi velit nibh, suscipit ac felis non, rhoncus aliquet eros.</p>
  <div class="brand">MERIDANE<br>Properties</div><div class="corner"></div>
</section>

<!-- Icon columns -->
<section class="slide sm" style="left:61px;top:632px">
  <div class="title">Lorem ipsum dolor sit amet</div>
  <div class="ic" style="left:12px"><div class="bar"><span class="sq"></span><span class="lab">Lorem<br>ipsum</span></div><p class="tiny">Lorem ipsum dolor sit amet, consectetur adipiscing elit. Nam sit amet dictum neque, pretium fringilla metus. Nam bibendum urna in pharetra vehicula.</p></div>
  <div class="ic" style="left:68px"><div class="bar"><span class="sq"></span><span class="lab">Lorem<br>ipsum</span></div><p class="tiny">Lorem ipsum dolor sit amet, consectetur adipiscing elit. Nam sit amet dictum neque, pretium fringilla metus. Nam bibendum urna in pharetra vehicula.</p></div>
  <div class="ic" style="left:124px"><div class="bar"><span class="sq"></span><span class="lab">Lorem<br>ipsum</span></div><p class="tiny">Lorem ipsum dolor sit amet, consectetur adipiscing elit. Nam sit amet dictum neque, pretium fringilla metus. Nam bibendum urna in pharetra vehicula.</p></div>
  <div class="ic" style="left:180px"><div class="bar"><span class="sq"></span><span class="lab">Lorem<br>ipsum</span></div><p class="tiny">Lorem ipsum dolor sit amet, consectetur adipiscing elit. Nam sit amet dictum neque, pretium fringilla metus. Nam bibendum urna in pharetra vehicula.</p></div>
  <div class="brand">MERIDANE<br>Properties</div><div class="corner"></div>
</section>

<!-- Table -->
<section class="slide sm tbl" style="left:341px;top:632px">
  <div class="title">Lorem ipsum dolor sit amet</div>
  <div class="photo thumb" style="left:60px;background:linear-gradient(160deg,#7b2b24,#3d2622)" role="img" aria-label="Photo of a red interior"></div>
  <div class="photo thumb" style="left:102px;background:linear-gradient(160deg,#b04a3a,#2d2a2a)" role="img" aria-label="Photo of a kitchen"></div>
  <div class="photo thumb" style="left:144px;background:linear-gradient(160deg,#8d5a48,#3b3433)" role="img" aria-label="Photo of a lounge"></div>
  <div class="photo thumb" style="left:186px;background:linear-gradient(160deg,#c9c1b6,#6b5a4e)" role="img" aria-label="Photo of a living area"></div>
  <div class="abs" style="left:14px;top:72px;width:45px;height:80px;background:#c9c9c9"></div>
  <div class="abs" style="left:59px;top:72px;width:171px;height:80px;background:#f2f2f2"></div>
  <span class="abs tiny w" style="left:16px;top:73px">Table 1</span>
  <div class="row" style="top:80px"></div><div class="row" style="top:88px"></div><div class="row" style="top:96px"></div><div class="row" style="top:104px"></div><div class="row" style="top:112px"></div><div class="row" style="top:120px"></div><div class="row" style="top:128px"></div><div class="row" style="top:136px"></div><div class="row" style="top:144px"></div>
  <div class="brand">MERIDANE<br>Properties</div><div class="corner"></div>
</section>

<!-- Charts -->
<section class="slide sm" style="left:619px;top:632px">
  <div class="title">Lorem ipsum dolor sit amet</div>
  <div class="hdr" style="left:10px;top:38px;width:104px"></div>
  <div class="hdr" style="left:125px;top:38px;width:105px"></div>
  <svg class="abs" style="left:10px;top:48px" width="104" height="36" viewBox="0 0 104 36">
    <g stroke="#ddd" stroke-width=".3"><line x1="4" y1="6" x2="104" y2="6"/><line x1="4" y1="14" x2="104" y2="14"/><line x1="4" y1="22" x2="104" y2="22"/><line x1="4" y1="30" x2="104" y2="30"/></g>
    <g fill="var(--red)"><rect x="10" y="14" width="3" height="16"/><rect x="34" y="18" width="3" height="12"/><rect x="58" y="16" width="3" height="14"/><rect x="82" y="10" width="3" height="20"/></g>
    <g fill="#222"><rect x="14" y="22" width="3" height="8"/><rect x="38" y="10" width="3" height="20"/><rect x="62" y="20" width="3" height="10"/><rect x="86" y="18" width="3" height="12"/></g>
    <g fill="#bbb"><rect x="18" y="26" width="3" height="4"/><rect x="42" y="26" width="3" height="4"/><rect x="66" y="22" width="3" height="8"/><rect x="90" y="14" width="3" height="16"/></g>
    <g font-size="2.6" fill="#777" font-family="Montserrat,sans-serif"><text x="8" y="34">Category 1</text><text x="32" y="34">Category 2</text><text x="56" y="34">Category 3</text><text x="80" y="34">Category 4</text></g>
  </svg>
  <svg class="abs" style="left:125px;top:48px" width="105" height="36" viewBox="0 0 105 36">
    <g stroke="#ddd" stroke-width=".3"><line x1="2" y1="6" x2="105" y2="6"/><line x1="2" y1="14" x2="105" y2="14"/><line x1="2" y1="22" x2="105" y2="22"/><line x1="2" y1="30" x2="105" y2="30"/></g>
    <polyline points="14,12 38,20 62,14 86,9" fill="none" stroke="var(--red)" stroke-width=".8"/>
    <polyline points="14,20 38,10 62,22 86,16" fill="none" stroke="#222" stroke-width=".8"/>
    <polyline points="14,26 38,24 62,18 86,20" fill="none" stroke="#999" stroke-width=".8"/>
    <g font-size="2.6" fill="#777" font-family="Montserrat,sans-serif"><text x="8" y="34">Category 1</text><text x="32" y="34">Category 2</text><text x="56" y="34">Category 3</text><text x="80" y="34">Category 4</text></g>
  </svg>
  <div class="hdr" style="left:10px;top:94px;width:104px;height:6px"></div>
  <div class="hdr" style="left:125px;top:94px;width:105px;height:6px"></div>
  <svg class="abs" style="left:30px;top:102px" width="70" height="36" viewBox="0 0 70 36">
    <circle cx="22" cy="18" r="12" fill="none" stroke="#ddd" stroke-width="5"/>
    <circle cx="22" cy="18" r="12" fill="none" stroke="var(--red)" stroke-width="5" stroke-dasharray="50 75" transform="rotate(-90 22 18)"/>
    <circle cx="22" cy="18" r="12" fill="none" stroke="#222" stroke-width="5" stroke-dasharray="10 75" stroke-dashoffset="-50" transform="rotate(-90 22 18)"/>
    <g font-size="3" fill="#444" font-family="Montserrat,sans-serif"><text x="48" y="10">● 1st Qtr</text><text x="48" y="16">● 2nd Qtr</text><text x="48" y="22">● 3rd Qtr</text><text x="48" y="28">● 4th Qtr</text></g>
  </svg>
  <div class="abs tiny" style="left:125px;top:101px;width:105px;display:flex;font-weight:600"><span style="flex:1;padding-left:2px">Title</span><span style="flex:1">Title</span><span style="flex:1">Title</span></div>
  <div class="abs" style="left:125px;top:107px;width:105px;height:44px;background:repeating-linear-gradient(180deg,#f3f3f3 0 5.5px,#fff 5.5px 11px)"></div>
  <div class="brand">MERIDANE<br>Properties</div><div class="corner"></div>
</section>

<!-- Thank you -->
<section class="slide sm thanks" style="left:898px;top:632px">
  <div class="photo shot" role="img" aria-label="Photo of modern white townhouses under a blue sky"></div>
  <div class="abs bye">Thank You</div>
  <div class="abs" style="left:10px;top:133px;font-size:6px;font-weight:700;color:var(--red);line-height:1.05">MERIDANE<br>Properties</div>
  <p class="abs tiny" style="left:48px;top:131px;width:180px;font-size:3px"><b style="color:var(--red)">Head Office</b><br>18 Harbor Road, Eastgate West, Johannesburg, 2090<br>Tel: +27 11 555 0142 / Fax: +27 11 555 0143<br>For enquiries, email us on info@meridane.com / visit our website on www.meridane.com</p>
  <div class="abs strip"></div><div class="abs strip2"></div>
</section>

</body>
</html>
```